Two (2) Merchant Advance Banner Ads

I need two (2) ads with rotating gif with 3 transitions for http://fundlinker.com/

Ad Specs:
Ad 1 must be an image equal to 250x250 pixels for website and email newsletter. .jpg, .gif, and
.png okay. No Flash!

Ad 2 must be an image equal to 720x90 pixels for website and mobile device view. .jpg, .gif, and
.png only. No Flash!

Client: Harwick Funding Partners merchant cash advance company out of Chicago. They provide alternative (to a bank loan) financing for small business owners across the U.S.
Here's their website: www.harwickfp.com

Purpose: Recruit 3rd party sellers of alternative financing. There are many sales financing professionals already out there soliciting small businesses, we want them to make a decision to sell Harwick's financing product to small businesses.

Copy:
Real People.
Competitive Commissions.
Great Rates.

I would like the logo (attached), phone number and CTA button to appear on all three transitions.
Call (888) 417-2859
Button: Get Started

Style:
Either something clean and simple, or something similar (not identifcal) to ads attached.
Brand standards guide is attached. Please use colors from guide.

```html
<!DOCTYPE html>
<html lang="en">
<head>
<meta charset="utf-8">
<title>Harwick Funding Partners – Banner Ads</title>
<link href="https://fonts.googleapis.com/css2?family=Nunito+Sans:ital,wght@0,400;0,600;0,700;0,800;1,800&family=Oswald:wght@400&display=swap" rel="stylesheet">
<style>
  :root{
    --canvas:#f2f2f2;
    --slate:#4b5866;
    --lime:#b3c236;
    --mint:#e0f98e;
    --teal:#19a3b2;
    --cyan:#00c6e4;
    --frame-a:#8d97a4;
    --frame-b:#e4e8ee;
    --frame-c:#6f7a88;
    --white:#ffffff;
  }
  *{box-sizing:border-box;margin:0;padding:0}
  html,body{width:1200px;height:1000px;overflow:hidden}
  body{background:var(--canvas);position:relative;font-family:"Nunito Sans",Arial,sans-serif;color:var(--slate)}

  .ad{position:absolute;padding:5px;
    background:linear-gradient(135deg,var(--frame-a),var(--frame-b) 30%,var(--frame-c) 55%,var(--frame-b) 80%,var(--frame-a));
    box-shadow:0 10px 14px rgba(0,0,0,.22)}
  .ad-inner{position:relative;width:100%;height:100%;background:var(--white);overflow:hidden}

  .leaderboard{left:240px;width:720px;height:90px}
  .leaderboard.one{top:128px}
  .leaderboard.two{top:293px}
  .leaderboard.three{top:458px}

  .square{top:623px;width:250px;height:250px}
  .square.one{left:125px}
  .square.two{left:475px}
  .square.three{left:825px}

  .brand-name{position:absolute;font-weight:700;color:var(--slate);text-align:center;line-height:1.05}
  .leaderboard .brand-name{left:10px;top:19px;width:130px;font-size:19px}
  .square .brand-name{left:45px;top:22px;width:150px;font-size:20px}

  .photo{position:absolute;background:linear-gradient(100deg,#e9ecef 0%,#d3d6da 30%,#3b3f45 55%,#c9b7a6 62%,#e8eaed 75%,#2f3338 100%)}
  .leaderboard .photo{left:415px;top:0;width:295px;height:80px}
  .square .photo{left:0;top:95px;width:240px;height:145px;
    background:linear-gradient(180deg,#eef0f2 0%,#dfe2e5 45%,#b9a898 70%,#e6e8ea 100%)}

  .panel-shape{position:absolute;left:0;top:0}

  .message{position:absolute;text-align:center;color:var(--slate)}
  .leaderboard .message{left:155px;width:265px;top:0;height:80px;display:flex;flex-direction:column;justify-content:center;align-items:center}
  .headline-small{font-size:16px;font-weight:400;line-height:1.1}
  .headline-small b{color:var(--lime);font-weight:800}
  .headline-big{font-size:20px;font-weight:800;line-height:1.1;color:var(--lime)}
  .headline-big i{color:var(--slate)}
  .stack-line{font-size:15.5px;line-height:1.4}

  .checklist{list-style:none;text-align:left}
  .checklist li{display:flex;align-items:center;gap:14px;font-size:14px;letter-spacing:.3px;height:23px}
  .tick{width:22px;height:22px;flex:none}

  .square .message{left:0;width:240px}
  .phone{font-size:15.5px;font-weight:700}

  .cta{position:absolute;padding:3px;background:linear-gradient(135deg,#c5ccd5,#8a95a3);}
  .cta span{display:block;background:var(--cyan);color:var(--white);font-family:"Oswald","Arial Narrow",sans-serif;font-size:15px;text-align:center;line-height:22px}
  .leaderboard .cta{left:545px;top:52px;width:94px}
  .square .cta{left:77px;top:212px;width:96px}
  .square .cta span{line-height:23px}

  .funding-badge{position:absolute;right:-2px;top:-1px;width:50px;height:50px;border-radius:50%;background:var(--lime);color:var(--white);text-align:center;padding-top:8px}
  .funding-badge .big{font-size:15px;line-height:1}
  .funding-badge .tiny{font-size:7px;line-height:1.2;display:block}

  .overlay-band{position:absolute;left:0;top:120px;width:240px;height:50px;background:rgba(255,255,255,.75)}
</style>
</head>
<body>

<svg width="0" height="0" style="position:absolute">
  <defs>
    <symbol id="tick-box" viewBox="0 0 22 22">
      <rect x="1.5" y="5.5" width="15" height="15" fill="none" stroke="#19a3b2" stroke-width="2"/>
      <path d="M4.5 12.5 L9 17 L20 2" fill="none" stroke="#00c6e4" stroke-width="3" stroke-linecap="round" stroke-linejoin="round"/>
    </symbol>
  </defs>
</svg>

<!-- Leaderboard 1 -->
<div class="ad leaderboard one">
  <div class="ad-inner">
    <div class="photo" role="img" aria-label="Photo of two businessmen in suits shaking hands"></div>
    <svg class="panel-shape" width="710" height="80" viewBox="0 0 710 80">
      <path d="M150 0 Q172 40 150 80 L430 80 Q408 40 430 0 Z" fill="#ffffff"/>
      <path d="M150 0 Q172 40 150 80" fill="none" stroke="#19a3b2" stroke-width="4"/>
      <path d="M430 0 Q408 40 430 80" fill="none" stroke="#19a3b2" stroke-width="4"/>
    </svg>
    <div class="brand-name">Harwick Funding Partners</div>
    <div class="message">
      <div class="headline-small">Small <b>BUSINESS</b></div>
      <div class="headline-big">BIG <i>IMPACT</i></div>
    </div>
    <div class="cta"><span>Get Started</span></div>
  </div>
</div>

<!-- Leaderboard 2 -->
<div class="ad leaderboard two">
  <div class="ad-inner">
    <div class="photo" role="img" aria-label="Photo of two businessmen in suits shaking hands"></div>
    <svg class="panel-shape" width="710" height="80" viewBox="0 0 710 80">
      <path d="M150 0 Q172 40 150 80 L430 80 Q408 40 430 0 Z" fill="#e0f98e"/>
      <path d="M150 0 Q172 40 150 80" fill="none" stroke="#19a3b2" stroke-width="4"/>
      <path d="M430 0 Q408 40 430 80" fill="none" stroke="#19a3b2" stroke-width="4"/>
    </svg>
    <div class="brand-name">Harwick Funding Partners</div>
    <div class="message">
      <ul class="checklist">
        <li><svg class="tick"><use href="#tick-box"/></svg>SIMPLE</li>
        <li><svg class="tick"><use href="#tick-box"/></svg>UNCOMPLICATED</li>
        <li><svg class="tick"><use href="#tick-box"/></svg>CONVENIENT</li>
      </ul>
    </div>
    <div class="cta"><span>Get Started</span></div>
  </div>
</div>

<!-- Leaderboard 3 -->
<div class="ad leaderboard three">
  <div class="ad-inner">
    <div class="photo" role="img" aria-label="Photo of two businessmen in suits shaking hands"></div>
    <svg class="panel-shape" width="710" height="80" viewBox="0 0 710 80">
      <path d="M150 0 Q172 40 150 80 L430 80 Q408 40 430 0 Z" fill="#e0f98e"/>
      <path d="M150 0 Q172 40 150 80" fill="none" stroke="#19a3b2" stroke-width="4"/>
      <path d="M430 0 Q408 40 430 80" fill="none" stroke="#19a3b2" stroke-width="4"/>
    </svg>
    <div class="brand-name">Harwick Funding Partners</div>
    <div class="message">
      <div class="stack-line">Real People.</div>
      <div class="stack-line">Competitive Commissions.</div>
      <div class="stack-line">Great Rates.</div>
    </div>
    <div class="cta"><span>Get Started</span></div>
  </div>
</div>

<!-- Square 1 -->
<div class="ad square one">
  <div class="ad-inner">
    <div class="photo" role="img" aria-label="Photo of two businessmen shaking hands"></div>
    <svg class="panel-shape" width="240" height="240" viewBox="0 0 240 240">
      <path d="M0 0 H240 V100 Q120 80 0 100 Z" fill="#ffffff"/>
      <path d="M0 100 Q120 80 240 100" fill="none" stroke="#19a3b2" stroke-width="4"/>
    </svg>
    <div class="overlay-band"></div>
    <div class="brand-name">Harwick Funding Partners</div>
    <div class="funding-badge"><span class="big">GET</span><span class="tiny">FUNDING</span></div>
    <div class="message" style="top:123px">
      <div class="headline-small">Small <b>BUSINESS</b></div>
      <div class="headline-big">BIG <i>IMPACT</i></div>
    </div>
    <div class="message phone" style="top:180px;color:#ffffff;font-weight:400">Call (888) 417-2859</div>
    <div class="cta"><span>Get Started</span></div>
  </div>
</div>

<!-- Square 2 -->
<div class="ad square two">
  <div class="ad-inner">
    <svg class="panel-shape" width="240" height="240" viewBox="0 0 240 240">
      <path d="M0 100 Q120 80 240 100 V240 H0 Z" fill="#e0f98e"/>
      <path d="M0 100 Q120 80 240 100" fill="none" stroke="#19a3b2" stroke-width="4"/>
    </svg>
    <div class="brand-name">Harwick Funding Partners</div>
    <div class="funding-badge"><span class="big">GET</span><span class="tiny">FUNDING</span></div>
    <div class="message" style="top:104px;display:flex;justify-content:center">
      <ul class="checklist">
        <li><svg class="tick"><use href="#tick-box"/></svg>SIMPLE</li>
        <li><svg class="tick"><use href="#tick-box"/></svg>UNCOMPLICATED</li>
        <li><svg class="tick"><use href="#tick-box"/></svg>CONVENIENT</li>
      </ul>
    </div>
    <div class="message phone" style="top:178px">Call (888) 417-2859</div>
    <div class="cta"><span>Get Started</span></div>
  </div>
</div>

<!-- Square 3 -->
<div class="ad square three">
  <div class="ad-inner">
    <svg class="panel-shape" width="240" height="240" viewBox="0 0 240 240">
      <path d="M0 100 Q120 80 240 100 V240 H0 Z" fill="#e0f98e"/>
      <path d="M0 100 Q120 80 240 100" fill="none" stroke="#19a3b2" stroke-width="4"/>
    </svg>
    <div class="brand-name">Harwick Funding Partners</div>
    <div class="funding-badge"><span class="big">GET</span><span class="tiny">FUNDING</span></div>
    <div class="message" style="top:101px">
      <div class="stack-line">Real People.</div>
      <div class="stack-line">Competitive Commissions.</div>
      <div class="stack-line">Great Rates.</div>
    </div>
    <div class="message phone" style="top:178px">Call (888) 417-2859</div>
    <div class="cta"><span>Get Started</span></div>
  </div>
</div>

</body>
</html>
```